Healthy Vending Machine Business Flyer

A modorn design that represents our healthy vending machine business. We will attach a picture of the machine we want on the flyer along with our logo. We will also upload the wording we want on the flyer

Colors

Designer to choose colors to be used in the design.

Requirements
Must have
• Flyer wording
• Front of flyer:
• (Picture of vending machine on the front)
• Free healthy vending machines hit the Treasure Valley
• Keep your Employees happy & productive with healthy vending options at work
• • No Cost to Your Company
• • Remote tracking tells us when your favorite snacks are running low
• • Credit Card/Smartphone Payment Technology
• • Ability to Customize your Snacks and Drinks
• • Locally Owned and Operated
• • Delicious Healthy Options
• Back of flyer:
• 431 Crispleaf Vending is a locally owned and operated company dedicated to making healthy snacks and drinks easily available for the Treasure Valley. We provide the latest in vending machine technology accepting credit cards, tillo wallet, and norvex wallet. State of the art inventory tracking tells us when your machine is running low so you're never out of your favorite drink or snack. We offer flexible stocking based on your companies needs and work with you on what items you want in the machine. Our goal is to give your employees and clients healthy options on the go
• To be considered for this FREE service for your business please visit: 431crispleafvending.com
• Or call/email today:
• Phone: 431-555-0162
• Email: 431crispleafvending@mailtrove.com
Should not have
• Any Additional Fruit images besides what is on the machine image.

```html
<!DOCTYPE html>
<html lang="en">
<head>
<meta charset="utf-8">
<title>431 Crispleaf Vending Flyer</title>
<link href="https://fonts.googleapis.com/css2?family=Open+Sans:wght@300;400;600;700&family=Roboto+Condensed:wght@700&display=swap" rel="stylesheet">
<style>
:root{
  --stage:#2d2d2f;
  --green:#6fb83f;
  --green-light:#8cc84f;
  --green-dark:#4f9a2e;
  --orange:#f7a81b;
  --orange-deep:#f07f1e;
  --yellow:#fcd21c;
  --blue:#1f4b8f;
  --teal:#7fcdc4;
  --paper:#f3f3f2;
  --ink:#2a2a2a;
  --grey-text:#3d3d3d;
}
*{margin:0;padding:0;box-sizing:border-box}
html,body{width:1200px;height:889px;overflow:hidden;background:var(--stage)}
body{position:relative;font-family:'Open Sans',sans-serif}
.page{position:absolute;top:107px;width:470px;height:667px;overflow:hidden;background:var(--paper);box-shadow:0 6px 18px rgba(0,0,0,.55)}
.page--back{left:124px}
.page--front{left:623px}

/* back page */
.back-top{position:absolute;left:0;top:0;width:470px;height:367px;background:radial-gradient(circle at 70% 40%,var(--green-light),var(--green) 55%,var(--green-dark))}
.back-wave{position:absolute;left:0;top:0}
.back-heading{position:absolute;left:30px;top:38px;width:300px;color:#fff;font-weight:600;font-size:17.6px;line-height:25px;text-shadow:0 1px 2px rgba(0,0,0,.35)}
.back-about{position:absolute;left:30px;top:138px;width:211px;color:#fff;font-size:10.2px;line-height:14.5px;text-align:justify}
.contact-card{position:absolute;left:270px;top:145px;width:174px;height:183px;background:var(--orange);border-radius:8px;box-shadow:0 3px 6px rgba(0,0,0,.25);text-align:center;color:#1b1b1b;overflow:hidden}
.contact-card__tab{position:absolute;left:10px;top:0}
.contact-card__lead{margin-top:24px;color:#fff;font-weight:600;font-size:13px}
.contact-card__phone{font-family:'Roboto Condensed',sans-serif;font-weight:700;color:#fff;font-size:26px;line-height:30px;text-shadow:0 1px 2px rgba(0,0,0,.3)}
.contact-card__or{font-weight:700;font-size:11.5px;margin-top:4px}
.contact-card__email{font-weight:600;font-size:7.4px;margin-top:3px}
.contact-card__note{font-weight:700;font-size:11.5px;line-height:15.5px;margin-top:8px}
.contact-card__url{color:#fff;font-weight:700;font-size:12px;margin-top:6px;text-shadow:0 1px 2px rgba(0,0,0,.3)}
.photo{position:absolute;top:367px;height:144px}
.photo--customer{left:0;width:218px;background:linear-gradient(100deg,#c9c9c6,#9aa2a6 45%,#dfe3e4 70%,#7c8a90)}
.photo--keypad{left:221px;width:249px;background:linear-gradient(90deg,#3d3a37,#8b6f5b 35%,#dcdcdc 62%,#2b2b2b 78%,#555 100%)}
.back-tagline{position:absolute;left:240px;top:553px;width:220px;text-align:center;color:var(--grey-text);font-weight:300;font-size:15.5px;line-height:20px}
.social{position:absolute;top:614px;width:34px;height:34px;border-radius:50%;background:var(--green-dark)}
.social--a{left:318px}.social--b{left:361px}

/* brand mark */
.brand{position:absolute;display:flex;align-items:center;gap:7px;color:var(--orange-deep);font-weight:700}
.brand__dot{width:14px;height:14px;border-radius:50%;background:var(--green)}
.page--back .brand{left:30px;top:600px;font-size:19px}
.page--front .brand{left:258px;top:555px;font-size:16px}

/* front page */
.front-bg{position:absolute;left:0;top:0}
.front-title{position:absolute;left:37px;top:26px;color:#fff;font-weight:700;font-size:35px;line-height:41px;letter-spacing:.3px;text-shadow:1px 2px 3px rgba(0,0,0,.3)}
.machine{position:absolute;left:25px;top:181px;width:213px;height:396px;background:linear-gradient(90deg,#1c1c1c 0,#3a3a3a 28%,#b8262a 58%,#6aa534 78%,#c9302c 100%);clip-path:polygon(0 20px,72% 0,100% 20px,100% 95%,72% 100%,0 90%)}
.front-lead{position:absolute;left:264px;top:221px;width:200px;color:var(--grey-text);font-weight:300;font-size:17.6px;line-height:23px}
.perks{position:absolute;left:264px;top:336px;width:200px;list-style:none;color:#333;font-size:10.2px;line-height:13px}
.perks li{position:relative;padding-left:14px;margin-bottom:6.5px}
.perks li::before{content:"";position:absolute;left:0;top:2px;width:9px;height:9px;border-radius:50%;background:radial-gradient(circle at 35% 35%,#a6da74,var(--green-dark))}
.front-footer{position:absolute;left:0;bottom:0}
.front-contact{position:absolute;left:52px;top:635px;color:#fff;font-weight:700;font-style:italic;font-size:10px}
.front-contact b{font-family:'Roboto Condensed',sans-serif;font-style:normal;font-size:15px;margin-left:2px}
</style>
</head>
<body>

<section class="page page--back">
  <div class="back-top"></div>
  <svg class="back-wave" width="470" height="60" viewBox="0 0 470 60" aria-hidden="true">
    <path d="M236 0 C300 10 360 34 470 28 L470 0Z" fill="var(--orange)"/>
    <path d="M236 0 C300 14 370 42 470 30" fill="none" stroke="var(--yellow)" stroke-width="3"/>
    <path d="M330 36 C380 44 420 40 470 33" fill="none" stroke="var(--blue)" stroke-width="2"/>
  </svg>
  <h2 class="back-heading">To be considered for this FREE service for your business please visit: 431crispleafvending.com</h2>
  <p class="back-about">431 Crispleaf Vending is a locally owned and operated company dedicated to making healthy snacks and drinks easily available for the Treasure Valley. We provide the latest in vending machine technology accepting credit cards, tillo wallet, and norvex wallet. State of the art inventory tracking tells us when your machine is running low so you're never out of your favorite drink or snack. We offer flexible stocking based on your companies needs and work with you on what items you want in the machine. Our goal is to give your employees and clients healthy options on the go</p>
  <div class="contact-card">
    <svg class="contact-card__tab" width="154" height="18" viewBox="0 0 154 18" aria-hidden="true"><path d="M0 0 H154 C145 12 138 17 124 17 H30 C16 17 9 12 0 0Z" fill="var(--teal)"/></svg>
    <p class="contact-card__lead">call/email today:</p>
    <p class="contact-card__phone">431-555-0162</p>
    <p class="contact-card__or">or email</p>
    <p class="contact-card__email">431crispleafvending@mailtrove.com</p>
    <p class="contact-card__note">To be considered for this FREE service for your business please visit</p>
    <p class="contact-card__url">431crispleafvending.com</p>
  </div>
  <div class="photo photo--customer" role="img" aria-label="Photo of a woman choosing an item at a vending machine"></div>
  <div class="photo photo--keypad" role="img" aria-label="Close-up photo of a finger pressing a vending machine keypad"></div>
  <div class="brand"><span class="brand__dot"></span>431 Crispleaf Vending</div>
  <p class="back-tagline">Healthy vending options are now available in your area</p>
  <span class="social social--a"></span>
  <span class="social social--b"></span>
</section>

<section class="page page--front">
  <svg class="front-bg" width="470" height="667" viewBox="0 0 470 667" aria-hidden="true">
    <defs><linearGradient id="lower" x1="0" y1="0" x2="1" y2="0"><stop offset="0" stop-color="#f4f4f3"/><stop offset="1" stop-color="#d9d9d8"/></linearGradient></defs>
    <rect width="470" height="667" fill="url(#lower)"/>
    <path d="M0 0 H470 V133 L0 289Z" fill="var(--orange)"/>
  </svg>
  <h1 class="front-title">Free healthy Vending<br>Machines hit the<br>Treasure Valley</h1>
  <div class="machine" role="img" aria-label="Photo of a healthy snack and drink vending machine wrapped in fruit graphics"></div>
  <p class="front-lead">Keep your Employees happy &amp; productive with healthy vending options at work</p>
  <ul class="perks">
    <li>No Cost to Your Company</li>
    <li>Remote tracking tells us when your favorite snacks are running low</li>
    <li>Credit Card/Smartphone Payment Technology</li>
    <li>Ability to Customize your Snacks and Drinks</li>
    <li>Locally Owned and Operated</li>
    <li>Delicious Healthy Options</li>
  </ul>
  <div class="brand"><span class="brand__dot"></span>431 Crispleaf Vending</div>
  <svg class="front-footer" width="470" height="60" viewBox="0 0 470 60" aria-hidden="true">
    <path d="M0 42 C120 10 220 40 330 40 C400 40 440 26 470 12 V60 H0Z" fill="var(--yellow)"/>
    <path d="M0 48 C120 18 220 46 330 46 C400 46 440 34 470 20 V60 H0Z" fill="var(--green)"/>
    <path d="M0 34 C60 16 120 8 170 10 C110 12 60 22 0 40Z" fill="var(--orange-deep)"/>
    <path d="M260 38 C360 44 430 30 470 10 L470 16 C430 36 360 48 260 38Z" fill="var(--orange-deep)"/>
  </svg>
  <p class="front-contact">Contact us : <b>431-555-0162</b></p>
</section>

</body>
</html>
```